Coffee Package Design

We need a new package design for a coffee company. Need to be a mix between modern and classic design combined together. We are open to different ideas.
We changing our product name from Café Verlona to Café Rostelli. The picture upload
shows what the product looks like. We want something completely different. The name of the company should go on the back of the package.
Updates

Hello Everyone,

Please read description, we are going with a new name and design for the product.

Café Rostelli. Café Verlona is what we are replacing with Café Rostelli, we are looking for new

look and design, please submit new designs.

There is a change in the description. Please take out Premium coffee blend and replace with Italian Roast.                                    

Industry/Entity Type

Cafe

Requirements
Must have
• You can use up to 6 colors.
Please put these items on design: Café Rostelli (this is the product name), Regular Premium Blend Coffee, 100% Arabica,
Dumbrell & Sons (name of the company), Tyler, TX on the back of the package

The file uploaded is an example of one of our products and how the package film
is sized.

```html
<!DOCTYPE html>
<html lang="en">
<head>
<meta charset="utf-8">
<title>Café Rostelli – Italian Roast Package Front</title>
<link rel="stylesheet" href="https://fonts.googleapis.com/css2?family=Tinos:wght@700&family=Lato:wght@400&display=swap">
<style>
  :root {
    --backdrop: #ececef;
    --film-grey: #606063;
    --film-grey-dark: #4f4f52;
    --roast-red: #d8231b;
    --roast-red-dark: #c81912;
    --leaf-green: #0b7b3c;
    --leaf-green-dark: #076a32;
    --ink-light: #f2f2f2;
    --rule-light: rgba(255, 255, 255, 0.75);
    --ornament-tone: #9a9a9d;
  }

  * { margin: 0; padding: 0; box-sizing: border-box; }

  html, body {
    width: 1200px;
    height: 1000px;
    overflow: hidden;
    background: var(--backdrop);
  }

  .package-front {
    position: absolute;
    left: 340px;
    top: 142px;
    width: 544px;
    height: 688px;
    overflow: hidden;
  }

  .brand-panel {
    position: absolute;
    left: 0; top: 0;
    width: 100%;
    height: 421px;
    background: linear-gradient(180deg, var(--film-grey) 0%, var(--film-grey-dark) 100%);
  }

  .product-name {
    position: absolute;
    left: 0; right: 0;
    top: 176px;
    text-align: center;
    font-family: "Tinos", "Times New Roman", serif;
    font-style: normal;
    font-weight: 700;
    font-size: 56px;
    letter-spacing: 1px;
    line-height: 1;
    color: var(--ink-light);
  }

  .flourish {
    position: absolute;
    left: 153px;
    top: 298px;
    width: 242px;
    height: 54px;
    border-radius: 27px;
    background: radial-gradient(ellipse at center, var(--ornament-tone) 0%, var(--film-grey) 75%);
    opacity: 0.55;
  }

  .variety-band {
    position: absolute;
    left: 0; top: 421px;
    width: 100%;
    height: 123px;
    background: linear-gradient(180deg, var(--roast-red) 0%, var(--roast-red-dark) 100%);
  }

  .variety-band::before,
  .variety-band::after {
    content: "";
    position: absolute;
    left: 0; right: 0;
    height: 1px;
    background: var(--rule-light);
  }
  .variety-band::before { top: 4px; }
  .variety-band::after { bottom: 5px; }

  .variety-name {
    position: absolute;
    left: 0; right: 0;
    top: 44px;
    text-align: center;
    font-family: "Tinos", "Times New Roman", serif;
    font-weight: 700;
    font-size: 34px;
    letter-spacing: 1px;
    line-height: 1;
    color: var(--ink-light);
  }

  .details-band {
    position: absolute;
    left: 0; top: 544px;
    width: 100%;
    height: 144px;
    background: linear-gradient(180deg, var(--leaf-green) 0%, var(--leaf-green-dark) 100%);
  }

  .product-claims {
    position: absolute;
    left: 0; right: 0;
    top: 22px;
    list-style: none;
    text-align: center;
    font-family: "Lato", "Gill Sans", sans-serif;
    font-size: 16px;
    letter-spacing: 1px;
    line-height: 27px;
    color: var(--ink-light);
  }
</style>
</head>
<body>
  <main class="package-front">
    <section class="brand-panel">
      <h1 class="product-name">Café Rostelli</h1>
      <div class="flourish" role="img" aria-label="Decorative calligraphic flourish beneath the product name"></div>
    </section>

    <section class="variety-band">
      <h2 class="variety-name">ITALIAN ROAST</h2>
    </section>

    <section class="details-band">
      <ul class="product-claims">
        <li>FRESHLY ROASTED &amp; PACKED</li>
        <li>100% ARABICA COFFEE</li>
      </ul>
    </section>
  </main>
</body>
</html>
```